Korvath Building Limited needs a complete stationary

We need a complete stationary based on our attached logo. Stationary should be need and clean with some simple high class design. We are targeting global customers to serve construction work, manpower supply and equipment supply services. We believe in quality work, reasonable cost and on time delivery. Our all stationary should be match with our business nature.

Target Market(s)

word wide

Industry/Entity Type

Construction Company

Font styles to use
Sans Serif

Requirements
Must have
• Good looking, clean type and simple design
Nice to have
• any good design any good font
Should not have
• rough design

```html
<!DOCTYPE html>
<html lang="en">
<head>
<meta charset="utf-8">
<title>Korvath Building Limited — Stationery</title>
<link href="https://fonts.googleapis.com/css2?family=Roboto+Condensed:wght@400;500&family=Montserrat:wght@400;500;600&display=swap" rel="stylesheet">
<style>
  :root {
    --brand: #0d50a0;
    --brand-soft: #5f79b8;
    --paper: #ffffff;
    --board: #b8b8b8;
    --ghost: #e3ebf5;
    --ghost-line: #d3e0ef;
    --ink: #1a1a1a;
  }
  * { margin: 0; padding: 0; box-sizing: border-box; }
  html, body { width: 1200px; height: 1200px; overflow: hidden; background: var(--board); }
  .board { position: relative; width: 1200px; height: 1200px; font-family: "Roboto Condensed", sans-serif; }
  .item { position: absolute; box-shadow: 6px 8px 10px rgba(0,0,0,.28); }
  .brand-circle { position: absolute; border-radius: 50%; }
  .icon { width: 9px; height: 9px; fill: var(--brand); vertical-align: -1px; margin-right: 4px; }

  /* Business card front */
  .card-front { left: 74px; top: 54px; width: 316px; height: 190px; background: var(--paper); overflow: hidden; }
  .card-front .band { position: absolute; left: 0; top: 0; width: 100%; height: 86px; background: var(--brand); }
  .card-front .mark { left: 22px; top: 43px; width: 94px; height: 94px; background: var(--paper); border: 3px solid var(--brand); display: flex; align-items: center; justify-content: center; text-align: center; }
  .card-front .mark span { font-size: 12px; font-weight: 500; color: var(--brand); line-height: 1.15; text-transform: uppercase; }
  .card-front .name { position: absolute; left: 133px; top: 38px; font-size: 13.5px; color: #fff; }
  .card-front .role { position: absolute; left: 133px; top: 55px; font-size: 8.5px; color: #fff; }
  .card-front .mobile { position: absolute; left: 133px; top: 72px; font-size: 9.5px; color: #fff; }
  .card-front .mobile .icon { fill: #fff; }
  .card-front .address { position: absolute; left: 133px; top: 97px; font-size: 9px; line-height: 11px; color: var(--brand); }
  .card-front .lines { position: absolute; left: 133px; top: 136px; font-size: 9.5px; line-height: 12px; color: var(--ink); }
  .card-front .web { position: absolute; left: 19px; top: 160px; font-size: 9.5px; color: var(--ink); }

  /* Business card backs */
  .card-back { top: 54px; width: 316px; height: 190px; background: var(--brand); color: #fff; }
  .card-back.outlined { left: 454px; }
  .card-back.tinted { left: 835px; }
  .card-back .head { position: absolute; left: 18px; top: 18px; width: 281px; height: 38px; padding: 4px 9px; font-size: 11.2px; line-height: 15px; }
  .card-back .col { position: absolute; top: 57px; width: 140px; height: 115px; padding: 8px 9px; font-size: 8.6px; line-height: 12px; }
  .card-back .col.left { left: 18px; }
  .card-back .col.right { left: 159px; }
  .outlined .frame { position: absolute; left: 18px; top: 18px; width: 281px; height: 154px; border: 1.5px solid #fff; }
  .outlined .frame::before { content: ""; position: absolute; left: 0; right: 0; top: 36px; border-top: 1.5px solid #fff; }
  .outlined .frame::after { content: ""; position: absolute; left: 139px; top: 36px; bottom: 0; border-left: 1.5px solid #fff; }
  .tinted .head, .tinted .col { background: var(--brand-soft); }
  .tinted .head { height: 35px; }
  .tinted .col { top: 57px; width: 139px; height: 114px; color: #e6ecf7; }
  .tinted .col.right { left: 160px; padding-left: 37px; }

  /* Letterhead */
  .letterhead { left: 74px; top: 350px; width: 540px; height: 763px; background: var(--paper); font-family: "Montserrat", sans-serif; }
  .letterhead .header { position: absolute; left: 0; top: 0; width: 100%; height: 98px; background: var(--brand); }
  .letterhead .header .mark { left: 52px; top: 13px; width: 70px; height: 70px; border: 3px solid #fff; background: var(--brand); }
  .letterhead .company { position: absolute; left: 150px; top: 29px; font-size: 18.5px; font-weight: 500; color: #fff; letter-spacing: .1px; }
  .letterhead .contact { position: absolute; top: 57px; font-size: 8.6px; color: #fff; }
  .letterhead .contact .icon { fill: #fff; }
  .letterhead .ghost-mark { left: 176px; top: 304px; width: 188px; height: 188px; border: 6px solid var(--ghost-line); background: var(--ghost); opacity: .75; }
  .ghost-name { position: absolute; display: flex; align-items: center; justify-content: center; text-align: center; font-weight: 600; text-transform: uppercase; color: var(--ghost-line); line-height: 1.1; }
  .letterhead .ghost-name { left: 176px; top: 304px; width: 188px; height: 188px; font-size: 22px; color: #c4d5ea; }
  .letterhead .footer { position: absolute; left: 0; bottom: 0; width: 100%; height: 35px; background: var(--brand); color: #fff; font-size: 8.6px; display: flex; align-items: center; justify-content: center; }

  /* Envelopes */
  .envelope { left: 645px; width: 506px; height: 253px; background: var(--paper); font-family: "Montserrat", sans-serif; overflow: hidden; }
  .envelope.back { top: 420px; }
  .envelope.back .ghost-mark { left: 374px; top: 120px; width: 124px; height: 124px; border: 4px solid var(--ghost-line); background: var(--ghost); opacity: .7; }
  .envelope.back .ghost-name { left: 374px; top: 120px; width: 124px; height: 124px; font-size: 13.5px; color: #c4d5ea; }
  .envelope.front { top: 731px; }
  .envelope .flap { position: absolute; left: 0; top: 0; width: 506px; height: 70px; }
  .envelope .seal { left: 231px; top: 17px; width: 18px; height: 18px; background: var(--brand); }
  .envelope .seal-name { position: absolute; left: 255px; top: 21px; font-size: 8.5px; font-weight: 600; color: var(--brand); text-transform: uppercase; }
  .envelope .address { position: absolute; left: 0; top: 228px; width: 100%; text-align: center; font-size: 7.4px; color: var(--brand); }
</style>
</head>
<body>
<svg width="0" height="0" style="position:absolute">
  <defs>
    <symbol id="i-phone" viewBox="0 0 16 16"><path d="M1 6c0-3 3-4 7-4s7 1 7 4h-4V4.5H5V6zM3 7h10l2 7H1z"/></symbol>
    <symbol id="i-mobile" viewBox="0 0 16 16"><path d="M4 1h8v14H4zM5.5 2.5v9h5v-9z"/></symbol>
    <symbol id="i-fax" viewBox="0 0 16 16"><path d="M4 1h7v5H4zM1 6h14v9H1zM3 9h3v2H3z"/></symbol>
    <symbol id="i-mail" viewBox="0 0 16 16"><path d="M1 4h14v10H1zM2 5l6 5 6-5z"/></symbol>
    <symbol id="i-globe" viewBox="0 0 16 16"><path d="M8 1a7 7 0 1 0 0 14A7 7 0 0 0 8 1zm0 1.5c1 1 1.6 2.7 1.7 4.7H6.3C6.4 5.2 7 3.5 8 2.5zM2.6 7.2A5.5 5.5 0 0 1 5 3.1 8 8 0 0 0 4.8 7.2zm0 1.6h2.2c.1 1.6.5 3 1.2 4.1a5.5 5.5 0 0 1-3.4-4.1zM8 13.5c-1-1-1.6-2.7-1.7-4.7h3.4c-.1 2-.7 3.7-1.7 4.7zm3.2-6.3A8 8 0 0 0 11 3.1a5.5 5.5 0 0 1 2.4 4.1zm0 1.6h2.2a5.5 5.5 0 0 1-3.4 4.1c.7-1.1 1.1-2.5 1.2-4.1z"/></symbol>
  </defs>
</svg>

<main class="board">
  <!-- Business card front -->
  <section class="item card-front">
    <div class="band"></div>
    <div class="brand-circle mark"><span>Korvath<br>Building<br>Limited</span></div>
    <p class="name">Marcus Ellery</p>
    <p class="role">Director</p>
    <p class="mobile"><svg class="icon"><use href="#i-mobile"/></svg>(000) 514-2270</p>
    <p class="address">Suite 810-812, 8/F, Harbourline Tower<br>47 Calder Rd. North Point<br>Hong Kong</p>
    <p class="lines">
      <svg class="icon"><use href="#i-phone"/></svg>(000) 376-5100<br>
      <svg class="icon"><use href="#i-fax"/></svg>(000) 514-2270<br>
      <svg class="icon"><use href="#i-mail"/></svg>info@korvathbuilding.com
    </p>
    <p class="web"><svg class="icon"><use href="#i-globe"/></svg>www.korvathbuilding.com</p>
  </section>

  <!-- Business card back, outlined -->
  <section class="item card-back outlined">
    <div class="frame"></div>
    <p class="head">Lorem Ipsum is simply dummy text of the printing and typesetting industry. Lorem Ipsum has been the</p>
    <p class="col left">Lorem Ipsum is simply<br>dummy text of the<br>printing and<br>typesetting industry.<br>Lorem Ipsum has<br>been the industry's<br>standard dummy text<br>ever since the 1500s,</p>
    <p class="col right">Lorem Ipsum is simply<br>dummy text of the<br>printing and<br>typesetting industry.<br>Lorem Ipsum has<br>been the industry's<br>standard dummy text<br>ever since the 1500s,</p>
  </section>

  <!-- Business card back, tinted -->
  <section class="item card-back tinted">
    <p class="head">Lorem Ipsum is simply dummy text of the printing and typesetting industry. Lorem Ipsum has been the</p>
    <p class="col left">Lorem Ipsum is simply<br>dummy text of the<br>printing and<br>typesetting industry.<br>Lorem Ipsum has<br>been the industry's<br>standard dummy text<br>ever since the 1500s,</p>
    <p class="col right">Lorem Ipsum is simply<br>dummy text of the<br>printing and<br>typesetting industry.<br>Lorem Ipsum has<br>been the industry's<br>standard dummy text<br>ever since the 1500s,</p>
  </section>

  <!-- Letterhead -->
  <section class="item letterhead">
    <header class="header">
      <div class="brand-circle mark"></div>
      <h1 class="company">KORVATH BUILDING LIMITED</h1>
      <p class="contact" style="left:150px"><svg class="icon"><use href="#i-phone"/></svg>(000) 376-5100</p>
      <p class="contact" style="left:266px"><svg class="icon"><use href="#i-fax"/></svg>(000) 514-2270</p>
      <p class="contact" style="left:373px"><svg class="icon"><use href="#i-mail"/></svg>info@korvathbuilding.com</p>
    </header>
    <div class="brand-circle ghost-mark"></div>
    <p class="ghost-name">Korvath<br>Building<br>Limited</p>
    <footer class="footer">Suite 810-812, 8/F, Harbourline Tower, 47 Calder Rd. North Point, Hong Kong</footer>
  </section>

  <!-- Envelope, plain side -->
  <section class="item envelope back">
    <div class="brand-circle ghost-mark"></div>
    <p class="ghost-name">Korvath<br>Building<br>Limited</p>
  </section>

  <!-- Envelope, flap side -->
  <section class="item envelope front">
    <svg class="flap" viewBox="0 0 506 70"><path d="M2 0 L16 55 Q19 63 28 63 L478 63 Q487 63 490 55 L505 0" fill="none" stroke="#8a8a8a" stroke-width="1"/></svg>
    <div class="brand-circle seal"></div>
    <p class="seal-name">Korvath Building Limited</p>
    <p class="address">Suite 810-812, 8/F, Harbourline Tower, 47 Calder Rd. North Point, Hong Kong</p>
  </section>
</main>
</body>
</html>
```